Professional WordPress Website Design & Development for IT Consulting Company (Quennor)

We are an IT consulting company (Quennor) based in Germany and are looking for a professional, modern and scalable WordPress website design INCLUDING full coding (WordPress theme/template).

IMPORTANT:
We do NOT want only a design (eg Photoshop files).
We want a fully working, coded WordPress website that we can host and manage ourselves.

The uploaded files (PowerPoint, HTML, logo) are ONLY for rough orientation.
They do NOT represent the final structure but give an idea of our visual style.

---

## COMPANY STRUCTURE (IMPORTANT)

Currently we operate as:

* Quennor UG (limited liability)

Planned structure:

* Quennor Operations GmbH (main operating company)
* Quennor Holding GmbH
* optionally later: Quennor Capital GmbH

The website should be designed as a scalable group website, but currently focus on the main brand "Quennor".

---

## BUSINESS FOCUS (IMPORTANT)

Our main business is:
→ Managed Services (core focus)

Additional areas:

* IT Infrastructure (Virtuon, Cirrant, HyperNode)
* Windows Server/Client environments
* Cloud & Hybrid solutions
* Network, Firewall, VPN
* Data center operations, migrations and rollouts

The website should clearly communicate:
→ reliability, scalability, enterprise-level service quality

---

## DESIGN STYLE & VISUAL DIRECTION

We like the design direction from our uploaded PowerPoint.

IMPORTANT:

* We especially like the green checkered/grid-style background with dark/black gradient
* This style should be used as inspiration
* Colors: green + dark/black + modern IT style

Design should be:

* modern
* clean
* professional
* enterprise-level
* trustworthy
* not playful or overloaded

---

## TECHNICAL REQUIREMENTS

* WordPress (self-hosted)
* Full source code delivery (no proprietary lock-in)
* Custom theme or clean reusable theme
* Editable without developer
* Multilingual: German, English, Polish
* SEO-friendly
* Fast performance
* GDPR/DSVO compliant contact form

---

## RESPONSIVE DESIGN & ACCESSIBILITY

Must be optimized for:

* Desktop
* Tablet
* Mobile

Layout must adapt automatically.

Accessibility:

* Clear typography
* Good contrast
* Easy navigation
* Mobile-friendly usability

Mobile experience must be fully functional and professional.

---

## STRUCTURE (NO ONE-PAGE WEBSITE)

We want a structured website with pages and subpages.

MAIN NAVIGATION (HEADER):

* Home
* Managed Services (MAIN FOCUS)
* Services
* Solutions / Expertise
* Projects / News
* Resources
* Careers
* Company
* Contact

SUBNAVIGATION / SUBPAGES (examples):

Managed Services:

* Overview
* Service Models
* SLAs & Support
* Monitoring & Operations

Services:

* Virtuon
* Cirrant
* HyperNode
* Fenestra Server / Client
* DeployCore / Endpointa
* Network / Firewall / VPN

Solutions:

* Data Center
* Cloud / Hybrid
* Migration Projects
* Security / Zero Trust

Projects / News:

* Projects
* Opportunities
* Articles

Resources:

* Available Experts
* Freelancer / Partner
* Internal Staff

Careers:

* Open Positions
* Freelancer Opportunities

Company:

* About Us
* Group Structure
* Values
* References

---

## HEADER / FOOTER STRUCTURE

HEADER:

* Sticky header (always visible)
* Main navigation with dropdowns or mega menu
* Clean, structured layout

FOOTER:

* Legal pages (Imprint, Privacy, Terms)
* Contact information
* Possibly quick links
* Consistent across all pages

---

## SPECIAL FEATURES

1. PROJECT / NEWS SYSTEM

* publish projects
* project opportunities
* articles

2. RESOURCE SYSTEM

* freelancers
* partners
* internal staff

With:

* skills
* availability
* role
* location
* language

---

## IMAGES, ICONS & LICENSING

Stock images (eg iStock) may be used as placeholders.

IMPORTANT:

* We will purchase final licenses ourselves
* No Google images or unknown sources

Icons and illustrations are welcome but must be properly licensed.

At delivery:

* Full asset list required (images, icons, sources, licenses)

---

## DELIVERABLES

We expect:

* Fully working WordPress website
* Full source code
* Installation instructions
* Plugin list
* No hidden dependencies
* No forced subscriptions
* Full usage rights

---

## IMPORTANT

We want to pay ONCE and fully own everything.

---

## LANGUAGES

Content will be managed by us:

* German
* English
* Polish

---

## FILES

Uploaded files are only for inspiration.

---

We are looking for a long-term, scalable and professional solution suitable for enterprise customers.
Updates

Additional update regarding interactions, hover effects and animations:

HOVER EFFECTS

We would like to include subtle and modern hover effects across the website:

Cards (eg Open Positions, Projects): → slight green glow on hover → minimal lift effect (approx. 2–4px)

Navigation (header): → hover color should be green (NOT orange)

Footer links (Imprint, Privacy, Terms): → slightly brighter on hover

Social icons (LinkedIn, XING, Gigstrelo): → subtle glow and slight scale on hover

IMPORTANT: All hover effects must be consistent, clean and not exaggerated.

ACTIVE STATE (VERY IMPORTANT)

Navigation elements must clearly show when they are active (current page).

This applies to:

Header navigation footer left

Behavior:

Active links should remain highlighted (eg green color and/or subtle underline) Users should always clearly see which page they are currently on

IMPORTANT: Active and hover states must be visually consistent across the entire website.

ANIMATIONS / MICRO INTERACTIONS

The website should not feel static.

We would like subtle and professional animations, such as:

smooth transitions between elements minimal background movement (very subtle) soft UI interactions

IMPORTANT: No heavy, flashy or distracting animations.

The goal is a high-end, enterprise-level feel.

COUNTERS / KEY METRICS

We want animated key numbers, for example:

150+ clients 10+ years experience 24/7 support 99.9% uptime

Behavior:

numbers should count up when they come into view (on scroll) fast and smoothly (approx. 0. 5–1 seconds) animation should trigger only once

Overall goal: A modern, dynamic and high-quality website with subtle interactions, not a flashy or overloaded design.

Hi everyone,

I have uploaded additional reference files to give you a clearer idea of the direction we are aiming for.

IMPORTANT: These files are only meant as inspiration and guidance – they are NOT strict templates that must be copied 1:1.

What we particularly like:

Dark / black + green design Subtle grid / tech background (as seen in the PowerPoint) Clean, modern and professional enterprise IT style Structured layout (no one-page scrolling) LANGUAGE FLAGS (IMPORTANT UPDATE)

Please adjust the language selection as follows:

Order:

German (DE) English (EN) Polish (PL)

For ENGLISH: We do NOT want a standard flag.

Instead, please create a combined UK/US flag:

Diagonally split design One side showing the UK flag The other side showing the US flag

This should look clean and professional (not playful).

FOOTER (IMPORTANT)

Footer should be:

Minimal and clean (not large or heavy) Positioned at the very bottom

Include:

Legal Notice / Imprint / Privacy Policy / Data Protection / Terms and Conditions / Terms

And: © Quennor UG

Social icons:

LinkedIn XING Gigstrelo

Please remove:

Facebook Twitter Instagram LAYOUT NOTE

Please avoid duplicate sections (eg "About Us" appearing multiple times).

We prefer a clean and structured layout with clear sections.

Thank you very much – looking forward to your designs!

Ich brauche zusätzliche Tage um durchzusehen

Target Market(s)

Enterprise and mid-sized companies, especially in automotive, finance, technology and IT infrastructure environments.

Industry/Entity Type

IT Consulting / Managed Services / Enterprise IT

Coding

Coded - Design and coding required

Font styles to use
Sans Serif

Colors
0094D4
00A9DD
6FCCEA
C7EBF8
E9F6FB
00AB8E
00BBA5
67D7C9
C6EFE9
E9F9F6
59FF00
82FF00
B8FF75
E3FFCB
F4FFEA

Requirements
Must have
• - Fully coded WordPress website (not just design) - Self-hosted, no dependency on designer - Responsive (desktop, tablet, mobile) - Multilingual (German, English, Polish) - Editable without developer - Clean, modern enterprise design - Structured navigation with subpages (no one-page website) - GDPR-compliant contact form - Scalable structure for future company expansion (group structure)
Nice to have
• - Subtle modern animations (not overloaded) - Mega menu or structured dropdown navigation - Clean icon set and optional illustrations - Reusable page templates - Fast loading performance - SEO-friendly structure - Team presentation with profiles (management, internal staff, technical roles) - Integration of social links (LinkedIn, Xing, Gigstrelo)
Should not have
• - No one-page scrolling website - No overly colorful or playful design - No outdated or generic templates - No confusing or complex navigation - No cheap-looking stock-heavy layouts - No dependency on proprietary builders or subscriptions

```html
<!DOCTYPE html>
<html lang="en">
<head>
<meta charset="utf-8">
<title>Quennor – Homepage Layouts</title>
<link href="https://fonts.googleapis.com/css2?family=DM+Sans:wght@400;500;600;700&display=swap" rel="stylesheet">
<style>
:root{
  --board:#2b2b2b;
  --page:#0a0e0a;
  --green:#45a524;
  --green-bright:#4fdc4f;
  --green-soft:#3c8f22;
  --green-deep:#1d4a10;
  --teal:#1f4a3d;
  --white:#ffffff;
  --muted:#c9d3c9;
  --ink:#1b1b1b;
  --grey:#7a7a7a;
}
*{margin:0;padding:0;box-sizing:border-box}
html,body{width:705px;height:1200px;overflow:hidden;background:var(--board)}
body{font-family:"DM Sans",Arial,sans-serif;color:var(--white)}
.stage{position:absolute;left:0;top:0;width:1480px;height:2520px;transform:scale(0.47635);transform-origin:0 0}
.page{position:absolute;top:86px;width:587px;height:2348px;background:var(--page);overflow:hidden}
.page--home{left:103px}
.page--menu{left:790px}
.abs{position:absolute}

.flags{left:415px;top:11px;display:flex;gap:4px}
.flag{width:13px;height:13px;border-radius:2px;overflow:hidden}
.flag--de{background:linear-gradient(#111 33%,#d01818 33% 66%,#f2c200 66%)}
.flag--en{background:linear-gradient(135deg,#1e3a8a 50%,#c8102e 50%);position:relative}
.flag--en::after{content:"";position:absolute;inset:5px 0;background:#fff;opacity:.6}
.flag--pl{background:linear-gradient(#fff 50%,#d4213d 50%)}
.btn-contact{left:478px;top:11px;width:54px;height:15px;border-radius:3px;background:var(--green);font-size:5px;display:flex;align-items:center;justify-content:center;gap:3px}

.navbar{left:54px;top:35px;width:478px;height:41px;border:1px solid var(--green);border-radius:9px;background:rgba(0,0,0,.35);display:flex;align-items:center;padding:0 10px}
.brand{display:flex;align-items:center;gap:6px;font-weight:700;font-size:16px;color:var(--white)}
.brand-mark{width:14px;height:14px;background:var(--white);border-radius:2px}
.nav-links{margin-left:auto;display:flex;gap:10px;font-size:6.5px;font-weight:500;white-space:nowrap}
.nav-links .is-active{color:var(--green-bright)}
.dropdown{left:273px;top:70px;width:115px;height:130px;background:#0d130d;border:1px solid #233423;border-radius:4px;padding:14px 18px;font-size:6px;display:flex;flex-direction:column;gap:11px;white-space:nowrap}

.hero-shape{left:0;top:0}
.hero-art{left:270px;top:55px;width:317px;height:250px;border-radius:50%;background:radial-gradient(ellipse at 55% 45%,#6ee94a 0%,#2f9b1c 30%,rgba(20,70,10,.6) 60%,rgba(0,0,0,0) 75%)}
.eyebrow{left:54px;top:114px;font-size:8px;font-weight:500}
.hero-title{left:54px;top:126px;font-size:26.5px;line-height:29px;font-weight:700;letter-spacing:-.3px}
.hero-sub{left:54px;top:188px;font-size:9.5px;color:var(--green-bright)}
.hero-copy{left:54px;top:204px;width:210px;font-size:7.5px;line-height:13px}
.btn{height:20px;border-radius:3px;font-size:6.5px;font-weight:500;display:flex;align-items:center;justify-content:center;gap:5px}
.btn--green{background:var(--green);color:var(--white)}
.btn--white{background:var(--white);color:var(--green)}
.btn i{width:6px;height:6px;border-radius:50%;background:currentColor;display:block}
.btn--green i{background:var(--white)}

.sec-title{left:0;width:587px;text-align:center;font-size:23px;font-weight:700;color:var(--green-bright);letter-spacing:-.3px}
.sec-sub{left:0;width:587px;text-align:center;font-size:11.5px}

.photo{border-radius:8px}
.photo--servers{left:54px;top:411px;width:187px;height:201px;background:linear-gradient(160deg,#0c2748,#1a5fa8 45%,#081428)}
.photo--hand{left:138px;top:528px;width:156px;height:124px;background:linear-gradient(150deg,#1f3447,#3e6b8a 50%,#0d1620);border:2px solid #0a0e0a}
.bar{width:2px;background:var(--green-bright)}
.who-title{left:333px;top:424px;font-size:22px;font-weight:700;color:var(--green-bright)}
.who-lead{left:333px;top:451px;font-size:11.5px}
.who-copy{left:333px;top:473px;width:199px;font-size:6.8px;line-height:13.5px;text-align:justify}
.checklist{left:355px;top:524px;list-style:none;font-size:6.8px;display:flex;flex-direction:column;gap:8.6px}
.checklist li{position:relative}
.checklist li::before{content:"";position:absolute;left:-17px;top:1px;width:7px;height:7px;border-radius:50%;background:var(--green)}

.svc{top:769px;width:113px;height:158px;border-radius:8px;background:linear-gradient(160deg,#5a5a5a,#222 60%,#111)}
.svc--active{background:linear-gradient(180deg,#0b2a7a,#1e7de0 40%,#4aa8ff 55%,#0b1a40);border:2px solid var(--green)}
.svc-label{top:936px;width:113px;text-align:center;font-size:7px;font-weight:500}
.svc-label--active{color:var(--green-bright)}

.experts-band{left:0;top:1013px}
.experts-title{left:0;width:587px;top:1041px;text-align:center;font-size:22px;font-weight:700}
.experts-sub{left:0;width:587px;top:1070px;text-align:center;font-size:11px}
.expert-card{left:113px;top:1101px;width:362px;height:199px;background:var(--white);border-radius:14px;border:3px solid #e6f1e0}
.expert-name{left:139px;top:1122px;font-size:13px;font-weight:600;color:var(--ink)}
.expert-role{left:139px;top:1141px;font-size:8.5px;color:var(--green)}
.expert-copy{left:139px;top:1160px;width:143px;font-size:6.6px;line-height:12.5px;color:var(--grey);text-align:justify}
.expert-photo{left:305px;top:1108px;width:162px;height:185px;border-radius:0 10px 10px 0;background:linear-gradient(160deg,#0f3f6e,#2d6f9d 45%,#16283b)}
.dots{left:280px;top:1321px;display:flex;gap:3px}
.dots span{width:4px;height:4px;border-radius:50%;background:#2e5a20}
.dots span:first-child{background:#0a0e0a}

.feature{width:120px;text-align:center}
.f-icon{width:42px;height:42px;margin:0 auto 10px;border-radius:9px;background:var(--green);display:flex;align-items:center;justify-content:center}
.f-icon--light{background:var(--white)}
.f-title{font-size:8.6px;color:var(--green-bright);margin-bottom:4px}
.f-copy{font-size:6.6px;line-height:11.5px}

.proj{top:1783px;width:152px;height:224px;border-radius:8px;border:1px solid #263026;background:#0d120d;overflow:hidden}
.proj--active{border:2px solid var(--green)}
.proj-img{height:128px;background:linear-gradient(160deg,#4a4a4a,#1a1a1a)}
.proj--active .proj-img{background:linear-gradient(160deg,#1b2d7a,#5a4fb8 45%,#15204a)}
.proj-body{padding:12px 12px 0}
.proj-date{font-size:5.5px;color:var(--muted);margin-bottom:8px;padding-left:10px}
.proj-name{font-size:8.6px;margin-bottom:4px}
.proj-copy{font-size:6.4px;line-height:11px;color:var(--muted)}

.footer-shape{left:0;top:2080px}
.footer-brand{left:0;width:587px;top:2146px;display:flex;justify-content:center;align-items:center;gap:12px;font-size:36px;font-weight:700}
.footer-brand .brand-mark{width:36px;height:36px;border-radius:4px}
.footer-links{left:0;width:587px;top:2219px;display:flex;justify-content:center;gap:15px;font-size:6.8px}
.contact{top:2252px;display:flex;align-items:center;gap:9px;font-size:6.2px;line-height:11px}
.c-icon{width:16px;height:16px;border-radius:50%;background:var(--green);display:flex;align-items:center;justify-content:center}
.socials{left:260px;top:2294px;display:flex;gap:9px}
.socials span{width:16px;height:16px;border-radius:50%;background:var(--white)}
.legal{left:154px;top:2323px;display:flex;gap:16px;font-size:5.6px}
.legal .link{color:var(--green-bright)}
</style>
</head>
<body>
<div class="stage">

<section class="page page--home">
  <svg class="abs hero-shape" width="587" height="360" viewBox="0 0 587 360">
    <defs><linearGradient id="heroA" x1="0" y1="0" x2="1" y2="1"><stop offset="0" stop-color="#0c200a"/><stop offset=".55" stop-color="#1f5a12"/><stop offset="1" stop-color="#2c7a18"/></linearGradient></defs>
    <path d="M0 0H587V185Q470 345 240 336Q110 330 0 300Z" fill="url(#heroA)"/>
    <path d="M587 180Q470 345 240 340Q150 337 105 322" fill="none" stroke="#3fb325" stroke-width="9"/>
  </svg>
  <div class="abs hero-art" role="img" aria-label="Glowing green cloud server platform illustration"></div>
  <div class="abs flags"><span class="flag flag--de"></span><span class="flag flag--en"></span><span class="flag flag--pl"></span></div>
  <div class="abs btn-contact">Contact Us <span style="width:4px;height:4px;border-radius:50%;background:#fff;display:block"></span></div>
  <nav class="abs navbar">
    <div class="brand"><span class="brand-mark"></span>Quennor</div>
    <div class="nav-links"><span class="is-active">HOME</span><span>Managed Services ⌄</span><span>Solutions ⌄</span><span>Projects ⌄</span><span>Resources ⌄</span><span>Careers ⌄</span><span>Company ⌄</span></div>
  </nav>
  <p class="abs eyebrow">HIGH-END MANAGED IT SERVICES</p>
  <h1 class="abs hero-title">YOUR EXTERNAL<br>IT DEPARTMENT</h1>
  <p class="abs hero-sub">PROACTIVE, RELIABLE, SCALABLE</p>
  <p class="abs hero-copy">Professional IT infrastructure management for enterprise and mid-sized companies.</p>
  <a class="abs btn btn--green" style="left:54px;top:239px;width:106px">Get a Consultation <i></i></a>
  <a class="abs btn btn--white" style="left:169px;top:239px;width:91px">Our Services <i></i></a>

  <div class="abs photo photo--servers" role="img" aria-label="Server racks under glowing blue clouds"></div>
  <div class="abs bar" style="left:247px;top:438px;height:90px"></div>
  <div class="abs bar" style="left:253px;top:448px;height:80px"></div>
  <div class="abs photo photo--hand" role="img" aria-label="Open hand holding digital document icons"></div>
  <h2 class="abs who-title">WHO WE ARE</h2>
  <p class="abs who-lead">Experienced. Reliable. Scalable.</p>
  <p class="abs who-copy">Over 10 years of experience providing high-end IT solutions to automotive, finance, technology, and enterprise IT sectors.</p>
  <ul class="abs checklist"><li>Enterprise-Grade Reliability</li><li>Scalable Solutions</li><li>Security-First Approach</li><li>Dedicated Professionals</li><li>Proven Experience &amp; End-to-End Expertise</li></ul>
  <a class="abs btn btn--green" style="left:333px;top:616px;width:88px">Explore More <i></i></a>

  <h2 class="abs sec-title" style="top:712px">OUR CORE SERVICES</h2>
  <p class="abs sec-sub" style="top:741px">The backbone of your IT success</p>
  <div class="abs svc" style="left:54px" role="img" aria-label="Technician working at server rack"></div>
  <div class="abs svc svc--active" style="left:176px" role="img" aria-label="Cloud with streaming data lines"></div>
  <div class="abs svc" style="left:297px" role="img" aria-label="Hand with holographic infrastructure icon"></div>
  <div class="abs svc" style="left:419px" role="img" aria-label="Padlock over keyboard"></div>
  <p class="abs svc-label" style="left:54px">Managed Services</p>
  <p class="abs svc-label svc-label--active" style="left:176px">Cloud &amp; Hybrid Solutions</p>
  <p class="abs svc-label" style="left:297px">IT Infrastructure</p>
  <p class="abs svc-label" style="left:419px">IT Security</p>

  <svg class="abs experts-band" width="587" height="360" viewBox="0 0 587 360" role="img" aria-label="Green band with faint cloud circuitry">
    <defs><radialGradient id="bandA" cx=".5" cy=".2" r=".8"><stop offset="0" stop-color="#4fae2c"/><stop offset="1" stop-color="#2f7c17"/></radialGradient></defs>
    <path d="M0 0H587V280Q293 400 0 280Z" fill="url(#bandA)"/>
  </svg>
  <h2 class="abs experts-title">EXPERTS BEHIND YOUR SUCCESS</h2>
  <p class="abs experts-sub">Passionate professionals. Proven results</p>
  <div class="abs expert-card"></div>
  <p class="abs expert-name">LUKAS BRENNER</p>
  <p class="abs expert-role">CEO &amp; Founder</p>
  <p class="abs expert-copy">Sed ut perspiciatis unde omnis iste natus error sit voluptatem accusantium doloremque laudantium, totam rem aperiam, eaque ipsa quae.<br><br>Nemo enim ipsam voluptatem quia voluptas sit aspernatur.</p>
  <a class="abs btn btn--green" style="left:139px;top:1257px;width:88px">Explore More <i></i></a>
  <div class="abs expert-photo" role="img" aria-label="Portrait of the company founder in a server room"></div>
  <div class="abs dots"><span></span><span></span><span></span><span></span></div>

  <h2 class="abs sec-title" style="top:1430px">OUR FEATURES</h2>
  <p class="abs sec-sub" style="top:1460px">Smart features that drive real results.</p>
  <div class="abs feature" style="left:50px;top:1528px"><div class="f-icon"><svg width="22" height="18" viewBox="0 0 22 18" fill="#fff"><circle cx="11" cy="5" r="3"/><circle cx="4" cy="7" r="2.3"/><circle cx="18" cy="7" r="2.3"/><path d="M5 17q0-7 6-7t6 7z"/></svg></div><p class="f-title">150<sup>+</sup> HAPPY CLIENTS</p><p class="f-copy">Sed ut perspiciatis unde omnis iste natus error sit voluptatem accusantium dolore</p></div>
  <div class="abs feature" style="left:172px;top:1504px"><div class="f-icon f-icon--light"><svg width="22" height="18" viewBox="0 0 22 18" fill="#45a524"><rect x="3" y="9" width="4" height="8"/><rect x="9" y="6" width="4" height="11"/><rect x="15" y="9" width="4" height="8"/><circle cx="5" cy="4" r="1.6"/><circle cx="11" cy="2" r="1.6"/><circle cx="17" cy="4" r="1.6"/></svg></div><p class="f-title">10<sup>+</sup> YEARS EXPERIENCE</p><p class="f-copy">Sed ut perspiciatis unde omnis iste natus error sit voluptatem accusantium dolore</p></div>
  <div class="abs feature" style="left:294px;top:1528px"><div class="f-icon"><svg width="20" height="20" viewBox="0 0 20 20" fill="none" stroke="#fff" stroke-width="2"><circle cx="10" cy="10" r="7"/><path d="M7 10h6M10 7v6"/></svg></div><p class="f-title">24/7 SUPPORT</p><p class="f-copy">Sed ut perspiciatis unde omnis iste natus error sit voluptatem accusantium dolore</p></div>
  <div class="abs feature" style="left:415px;top:1504px"><div class="f-icon"><svg width="20" height="20" viewBox="0 0 20 20" fill="#fff"><path d="M10 2a8 8 0 1 0 8 8h-8z"/><rect x="12" y="2" width="2" height="6"/><rect x="15" y="4" width="2" height="4"/></svg></div><p class="f-title">99.9% UPTIME</p><p class="f-copy">Sed ut perspiciatis unde omnis iste natus error sit voluptatem accusantium dolore</p></div>

  <h2 class="abs sec-title" style="top:1720px">PROJECTS &amp; RESOURCES</h2>
  <p class="abs sec-sub" style="top:1750px">Where expertise meets execution</p>
  <article class="abs proj" style="left:54px"><div class="proj-img" role="img" aria-label="Cloud hologram above data center"></div><div class="proj-body"><p class="proj-date">15 Apr 2024</p><p class="proj-name">Data Center Migration</p><p class="proj-copy">Successful migration of critical systems and applications for a leading automotive client.</p></div></article>
  <article class="abs proj proj--active" style="left:217px"><div class="proj-img" role="img" aria-label="Engineer with tablet in front of code screens"></div><div class="proj-body"><p class="proj-date">18 Apr 2024</p><p class="proj-name">Zero Trust Security Model</p><p class="proj-copy">For Automotive Client, Restructuring security across the entire modern IT environment.</p></div></article>
  <article class="abs proj" style="left:380px"><div class="proj-img" role="img" aria-label="Developer at laptop with cloud hologram"></div><div class="proj-body"><p class="proj-date">15 Apr 2024</p><p class="proj-name">Data Center Migration</p><p class="proj-copy">Successful migration of critical systems and applications for a leading automotive client.</p></div></article>
  <a class="abs btn btn--green" style="left:250px;top:2026px;width:87px">Explore More <i></i></a>

  <svg class="abs footer-shape" width="587" height="270" viewBox="0 0 587 270">
    <path d="M0 268V190Q120 20 380 8Q500 4 587 25V268Z" fill="#1f4a3d"/>
    <path d="M0 195Q120 20 380 8Q470 4 520 12" fill="none" stroke="#3fb325" stroke-width="11"/>
  </svg>
  <div class="abs footer-brand"><span class="brand-mark"></span>Quennor</div>
  <nav class="abs footer-links"><span>Home</span><span>Managed Services</span><span>Services</span><span>Solutions</span><span>Projects</span><span>Resources</span><span>Careers</span><span>Company</span><span>Contact</span></nav>
  <div class="abs contact" style="left:110px"><span class="c-icon"><svg width="8" height="9" viewBox="0 0 8 9" fill="#fff"><path d="M4 0a3 3 0 0 0-3 3c0 2.5 3 6 3 6s3-3.5 3-6a3 3 0 0 0-3-3z"/></svg></span><p>Lindenweg 7<br>10115 Berlin, Germany</p></div>
  <div class="abs contact" style="left:260px"><span class="c-icon"><svg width="8" height="8" viewBox="0 0 8 8" fill="#fff"><path d="M1 0h2l1 2-1 1q1 2 2 2l1-1 2 1v2q-4 1-7-7z"/></svg></span><p>Phone Number:<br>+49 30 5550142-0</p></div>
  <div class="abs contact" style="left:387px"><span class="c-icon"><svg width="8" height="6" viewBox="0 0 8 6" fill="#fff"><path d="M0 0h8v6H0zM0 0l4 3 4-3" stroke="#45a524" stroke-width=".6"/></svg></span><p>Email Address:<br>contact@quennor.eu</p></div>
  <div class="abs socials"><span></span><span></span><span></span></div>
  <p class="abs legal"><span>(C) Copyright 2026 | All Rights Reserved</span><span class="link">IMPRINT</span><span class="link">|</span><span class="link">PRIVACY</span><span class="link">|</span><span class="link">TERMS</span></p>
</section>

<section class="page page--menu">
  <svg class="abs hero-shape" width="587" height="360" viewBox="0 0 587 360">
    <defs><linearGradient id="heroB" x1="0" y1="0" x2="1" y2="1"><stop offset="0" stop-color="#0c200a"/><stop offset=".55" stop-color="#1f5a12"/><stop offset="1" stop-color="#2c7a18"/></linearGradient></defs>
    <path d="M0 0H587V185Q470 345 240 336Q110 330 0 300Z" fill="url(#heroB)"/>
    <path d="M587 180Q470 345 240 340Q150 337 105 322" fill="none" stroke="#3fb325" stroke-width="9"/>
  </svg>
  <div class="abs hero-art" role="img" aria-label="Glowing green cloud server platform illustration"></div>
  <div class="abs flags"><span class="flag flag--de"></span><span class="flag flag--en"></span><span class="flag flag--pl"></span></div>
  <div class="abs btn-contact">Contact Us <span style="width:4px;height:4px;border-radius:50%;background:#fff;display:block"></span></div>
  <nav class="abs navbar">
    <div class="brand"><span class="brand-mark"></span>Quennor</div>
    <div class="nav-links"><span>Home</span><span>Managed Services ⌄</span><span class="is-active">SOLUTIONS ⌄</span><span>Projects ⌄</span><span>Resources ⌄</span><span>Careers ⌄</span><span>Company ⌄</span></div>
  </nav>
  <p class="abs eyebrow">HIGH-END MANAGED IT SERVICES</p>
  <h1 class="abs hero-title">YOUR EXTERNAL<br>IT DEPARTMENT</h1>
  <p class="abs hero-sub">PROACTIVE, RELIABLE, SCALABLE</p>
  <p class="abs hero-copy">Professional IT infrastructure management for enterprise and mid-sized companies.</p>
  <a class="abs btn btn--green" style="left:54px;top:239px;width:106px">Get a Consultation <i></i></a>
  <a class="abs btn btn--white" style="left:169px;top:239px;width:91px">Our Services <i></i></a>
  <div class="abs dropdown"><span>Virtuon</span><span>Cirrant</span><span>HyperNode</span><span>Fenestra Server / Client</span><span>DeployCore / Endpointa</span><span>Network / Firewall / VPN</span></div>

  <div class="abs photo photo--servers" role="img" aria-label="Server racks under glowing blue clouds"></div>
  <div class="abs bar" style="left:247px;top:438px;height:90px"></div>
  <div class="abs bar" style="left:253px;top:448px;height:80px"></div>
  <div class="abs photo photo--hand" role="img" aria-label="Open hand holding digital document icons"></div>
  <h2 class="abs who-title">WHO WE ARE</h2>
  <p class="abs who-lead">Experienced. Reliable. Scalable.</p>
  <p class="abs who-copy">Over 10 years of experience providing high-end IT solutions to automotive, finance, technology, and enterprise IT sectors.</p>
  <ul class="abs checklist"><li>Enterprise-Grade Reliability</li><li>Scalable Solutions</li><li>Security-First Approach</li><li>Dedicated Professionals</li><li>Proven Experience &amp; End-to-End Expertise</li></ul>
  <a class="abs btn btn--green" style="left:333px;top:616px;width:88px">Explore More <i></i></a>

  <h2 class="abs sec-title" style="top:712px">OUR CORE SERVICES</h2>
  <p class="abs sec-sub" style="top:741px">The backbone of your IT success</p>
  <div class="abs svc" style="left:54px" role="img" aria-label="Technician working at server rack"></div>
  <div class="abs svc svc--active" style="left:176px" role="img" aria-label="Cloud with streaming data lines"></div>
  <div class="abs svc" style="left:297px" role="img" aria-label="Hand with holographic infrastructure icon"></div>
  <div class="abs svc" style="left:419px" role="img" aria-label="Padlock over keyboard"></div>
  <p class="abs svc-label" style="left:54px">Managed Services</p>
  <p class="abs svc-label svc-label--active" style="left:176px">Cloud &amp; Hybrid Solutions</p>
  <p class="abs svc-label" style="left:297px">IT Infrastructure</p>
  <p class="abs svc-label" style="left:419px">IT Security</p>

  <svg class="abs experts-band" width="587" height="360" viewBox="0 0 587 360" role="img" aria-label="Green band with faint cloud circuitry">
    <defs><radialGradient id="bandB" cx=".5" cy=".2" r=".8"><stop offset="0" stop-color="#4fae2c"/><stop offset="1" stop-color="#2f7c17"/></radialGradient></defs>
    <path d="M0 0H587V280Q293 400 0 280Z" fill="url(#bandB)"/>
  </svg>
  <h2 class="abs experts-title">EXPERTS BEHIND YOUR SUCCESS</h2>
  <p class="abs experts-sub">Passionate professionals. Proven results</p>
  <div class="abs expert-card"></div>
  <p class="abs expert-name">LUKAS BRENNER</p>
  <p class="abs expert-role">CEO &amp; Founder</p>
  <p class="abs expert-copy">Sed ut perspiciatis unde omnis iste natus error sit voluptatem accusantium doloremque laudantium, totam rem aperiam, eaque ipsa quae.<br><br>Nemo enim ipsam voluptatem quia voluptas sit aspernatur.</p>
  <a class="abs btn btn--green" style="left:139px;top:1257px;width:88px">Explore More <i></i></a>
  <div class="abs expert-photo" role="img" aria-label="Portrait of the company founder in a server room"></div>
  <div class="abs dots"><span></span><span></span><span></span><span></span></div>

  <h2 class="abs sec-title" style="top:1430px">OUR FEATURES</h2>
  <p class="abs sec-sub" style="top:1460px">Smart features that drive real results.</p>
  <div class="abs feature" style="left:50px;top:1528px"><div class="f-icon"><svg width="22" height="18" viewBox="0 0 22 18" fill="#fff"><circle cx="11" cy="5" r="3"/><circle cx="4" cy="7" r="2.3"/><circle cx="18" cy="7" r="2.3"/><path d="M5 17q0-7 6-7t6 7z"/></svg></div><p class="f-title">150<sup>+</sup> HAPPY CLIENTS</p><p class="f-copy">Sed ut perspiciatis unde omnis iste natus error sit voluptatem accusantium dolore</p></div>
  <div class="abs feature" style="left:172px;top:1504px"><div class="f-icon f-icon--light"><svg width="22" height="18" viewBox="0 0 22 18" fill="#45a524"><rect x="3" y="9" width="4" height="8"/><rect x="9" y="6" width="4" height="11"/><rect x="15" y="9" width="4" height="8"/><circle cx="5" cy="4" r="1.6"/><circle cx="11" cy="2" r="1.6"/><circle cx="17" cy="4" r="1.6"/></svg></div><p class="f-title">10<sup>+</sup> YEARS EXPERIENCE</p><p class="f-copy">Sed ut perspiciatis unde omnis iste natus error sit voluptatem accusantium dolore</p></div>
  <div class="abs feature" style="left:294px;top:1528px"><div class="f-icon"><svg width="20" height="20" viewBox="0 0 20 20" fill="none" stroke="#fff" stroke-width="2"><circle cx="10" cy="10" r="7"/><path d="M7 10h6M10 7v6"/></svg></div><p class="f-title">24/7 SUPPORT</p><p class="f-copy">Sed ut perspiciatis unde omnis iste natus error sit voluptatem accusantium dolore</p></div>
  <div class="abs feature" style="left:415px;top:1504px"><div class="f-icon"><svg width="20" height="20" viewBox="0 0 20 20" fill="#fff"><path d="M10 2a8 8 0 1 0 8 8h-8z"/><rect x="12" y="2" width="2" height="6"/><rect x="15" y="4" width="2" height="4"/></svg></div><p class="f-title">99.9% UPTIME</p><p class="f-copy">Sed ut perspiciatis unde omnis iste natus error sit voluptatem accusantium dolore</p></div>

  <h2 class="abs sec-title" style="top:1720px">PROJECTS &amp; RESOURCES</h2>
  <p class="abs sec-sub" style="top:1750px">Where expertise meets execution</p>
  <article class="abs proj" style="left:54px"><div class="proj-img" role="img" aria-label="Cloud hologram above data center"></div><div class="proj-body"><p class="proj-date">15 Apr 2024</p><p class="proj-name">Data Center Migration</p><p class="proj-copy">Successful migration of critical systems and applications for a leading automotive client.</p></div></article>
  <article class="abs proj proj--active" style="left:217px"><div class="proj-img" role="img" aria-label="Engineer with tablet in front of code screens"></div><div class="proj-body"><p class="proj-date">18 Apr 2024</p><p class="proj-name">Zero Trust Security Model</p><p class="proj-copy">For Automotive Client, Restructuring security across the entire modern IT environment.</p></div></article>
  <article class="abs proj" style="left:380px"><div class="proj-img" role="img" aria-label="Developer at laptop with cloud hologram"></div><div class="proj-body"><p class="proj-date">15 Apr 2024</p><p class="proj-name">Data Center Migration</p><p class="proj-copy">Successful migration of critical systems and applications for a leading automotive client.</p></div></article>
  <a class="abs btn btn--green" style="left:250px;top:2026px;width:87px">Explore More <i></i></a>

  <svg class="abs footer-shape" width="587" height="270" viewBox="0 0 587 270">
    <path d="M0 268V190Q120 20 380 8Q500 4 587 25V268Z" fill="#1f4a3d"/>
    <path d="M0 195Q120 20 380 8Q470 4 520 12" fill="none" stroke="#3fb325" stroke-width="11"/>
  </svg>
  <div class="abs footer-brand"><span class="brand-mark"></span>Quennor</div>
  <nav class="abs footer-links"><span>Home</span><span>Managed Services</span><span>Services</span><span>Solutions</span><span>Projects</span><span>Resources</span><span>Careers</span><span>Company</span><span>Contact</span></nav>
  <div class="abs contact" style="left:110px"><span class="c-icon"><svg width="8" height="9" viewBox="0 0 8 9" fill="#fff"><path d="M4 0a3 3 0 0 0-3 3c0 2.5 3 6 3 6s3-3.5 3-6a3 3 0 0 0-3-3z"/></svg></span><p>Lindenweg 7<br>10115 Berlin, Germany</p></div>
  <div class="abs contact" style="left:260px"><span class="c-icon"><svg width="8" height="8" viewBox="0 0 8 8" fill="#fff"><path d="M1 0h2l1 2-1 1q1 2 2 2l1-1 2 1v2q-4 1-7-7z"/></svg></span><p>Phone Number:<br>+49 30 5550142-0</p></div>
  <div class="abs contact" style="left:387px"><span class="c-icon"><svg width="8" height="6" viewBox="0 0 8 6" fill="#fff"><path d="M0 0h8v6H0zM0 0l4 3 4-3" stroke="#45a524" stroke-width=".6"/></svg></span><p>Email Address:<br>contact@quennor.eu</p></div>
  <div class="abs socials"><span></span><span></span><span></span></div>
  <p class="abs legal"><span>(C) Copyright 2026 | All Rights Reserved</span><span class="link">IMPRINT</span><span class="link">|</span><span class="link">PRIVACY</span><span class="link">|</span><span class="link">TERMS</span></p>
</section>

</div>
</body>
</html>
```